Design a Flyer 1/2 Page in size with Coupons for Pizza Shop

I want a half page (2 to fit on one page in portrait orientation on letter paper 8.5x11)

I need an Corner Market logo small at the top, with the address 2718 County Line 84, Maplecrest Township (555) 014-2287
Then add in the Tolu Reno Logo into the top of the ad somehow. Use the entire portion to advertise for the Brand.
Have an impact 3d small graphic that says Fresh Dough
Include "Call Your Order In!"

Include the logo and pictures of our pizza from the files that I send you. You will have to photoshop out the background of some of the images of our pizza to make it work and look good.

The 4 coupons I want to be included on the bottom are as follows

Coupon 1

1 - 16" Extra Large 3 Topping Pizza
1 12” Medium Breadsticks with Cheese
$12.95

Coupon 2

14" Large Pepperoni Pizza $5.95

Coupon 3
Family Pizza Night
2 - 14" Large 2 topping Pizzas
1 - 12” Medium Breadsticks with Cheese
1 - 2 liter of Zesta
$15.95

Coupon 4
Pizza Lover’s Deal
3 - Medium 1 Topping Pizza’s
$11.99

Put an expiration date on the coupons of 5/31/2015

I need this really knocked out of the park. This is a store that is hurting for business and we need to really design up a good draw from this.

```html
<!DOCTYPE html>
<html lang="en">
<head>
<meta charset="utf-8">
<title>Tolu Reno Pizza – Coupon Flyer</title>
<link href="https://fonts.googleapis.com/css2?family=Alfa+Slab+One&family=Arimo:wght@700&family=Rammetto+One&display=swap" rel="stylesheet">
<style>
  :root {
    --paper: #f6cc6e;
    --paper-deep: #efbb52;
    --brand-red: #b5122b;
    --ink: #3a1a0c;
    --cream: #fff3b8;
    --white: #ffffff;
    --tag: #f3a91c;
    --tag-edge: #d98a0a;
    --cut-line: #fff1c9;
    --crust: #e2a45a;
    --sauce: #c9432a;
    --cheese: #f2c15a;
  }
  * { box-sizing: border-box; margin: 0; padding: 0; }
  html, body { width: 927px; height: 1200px; overflow: hidden; background: var(--paper); }
  .flyer {
    position: relative; width: 927px; height: 1200px; overflow: hidden;
    background: radial-gradient(ellipse at 50% 40%, var(--paper) 0%, var(--paper-deep) 100%);
    font-family: "Alfa Slab One", serif;
  }
  .abs { position: absolute; }

  .brand-logo {
    left: 30px; top: 40px; width: 450px; height: 200px;
    display: flex; align-items: center; gap: 18px;
  }
  .brand-logo .mark { width: 70px; height: 70px; border-radius: 50%; background: var(--brand-red); flex: none; }
  .brand-logo .name { font-family: "Alfa Slab One", serif; font-size: 58px; line-height: 1; color: var(--brand-red); }

  .partner { left: 620px; top: 60px; width: 280px; display: flex; align-items: center; justify-content: center; gap: 10px; }
  .partner .mark { width: 26px; height: 26px; background: var(--ink); flex: none; }
  .partner .name { font-family: "Arimo", sans-serif; font-size: 28px; color: var(--ink); white-space: nowrap; }

  .address {
    left: 600px; top: 130px; width: 300px; text-align: center; font-style: normal;
    font-family: "Arimo", sans-serif; font-size: 22px; line-height: 31px; color: var(--white);
    text-shadow: 0 0 2px var(--ink), 1px 1px 0 var(--ink), -1px -1px 0 var(--ink), 1px -1px 0 var(--ink), -1px 1px 0 var(--ink);
  }

  .red-display {
    color: var(--brand-red); font-weight: 400;
    -webkit-text-stroke: 1px var(--white);
    text-shadow: 2px 2px 0 var(--white), -2px -2px 0 var(--white), 2px -2px 0 var(--white), -2px 2px 0 var(--white), 4px 5px 3px rgba(58,26,12,.55);
  }
  .fresh-dough { left: 578px; top: 255px; font-size: 44px; }
  .custom-made { left: 0; width: 1000px; top: 337px; text-align: center; font-size: 21px; letter-spacing: .5px; }
  .menu-line { left: 0; width: 1000px; top: 360px; text-align: center; font-size: 38px; }
  .call-in { left: 22px; top: 432px; font-family: "Rammetto One", serif; font-size: 62px; letter-spacing: 1px; }

  .cut-h { left: 0; width: 927px; height: 0; border-top: 4px dashed var(--cut-line); }
  .cut-v { left: 463px; top: 598px; height: 602px; width: 0; border-left: 4px dashed var(--cut-line); }
  .scissors { left: 18px; top: 572px; }

  .price-tag {
    background: var(--tag); border: 2px solid var(--tag-edge); border-radius: 12px;
    transform: rotate(-9deg); display: flex; align-items: flex-start; justify-content: center;
    box-shadow: 3px 4px 6px rgba(58,26,12,.35);
    font-family: "Rammetto One", serif; color: var(--white);
    text-shadow: 0 0 3px var(--ink), 2px 2px 0 var(--ink);
  }
  .price-tag .dollars { font-size: 46px; line-height: 74px; }
  .price-tag .cents { font-size: 22px; line-height: 40px; }

  .food { border-radius: 50%; }
  .pizza { background: radial-gradient(circle, var(--sauce) 0%, var(--cheese) 55%, var(--crust) 85%); }
  .breadsticks { background: linear-gradient(135deg, #f0d38c, var(--crust)); border-radius: 40%; }
  .bottle { background: linear-gradient(90deg, #3b0c0c, #9d1b1b 50%, #3b0c0c); border-radius: 20px 20px 10px 10px; }

  .deal-title, .deal-line {
    color: var(--cream); font-size: 17px; white-space: nowrap;
    text-shadow: 0 0 2px var(--ink), 1px 1px 0 var(--ink), -1px -1px 0 var(--ink), 1px -1px 0 var(--ink), -1px 1px 0 var(--ink), 2px 3px 3px rgba(0,0,0,.4);
  }
  .deal-title { font-size: 19px; }
  .expires {
    font-family: "Alfa Slab One", serif; font-size: 14px; color: var(--white); white-space: nowrap;
    text-shadow: 0 0 2px var(--ink), 1px 1px 0 var(--ink), -1px -1px 0 var(--ink);
  }
</style>
</head>
<body>
<main class="flyer">

  <div class="abs brand-logo">
    <span class="mark"></span>
    <span class="name">Tolu Reno Pizza</span>
  </div>

  <div class="abs partner"><span class="mark"></span><span class="name">Corner Market</span></div>

  <address class="abs address">
    2718 County Line 84,<br>Maplecrest Township<br>(555) 014-2287
  </address>

  <div class="abs red-display fresh-dough">Fresh Dough</div>
  <div class="abs red-display custom-made">CUSTOM MADE</div>
  <div class="abs red-display menu-line">Pizza, Subs &amp; Hoagies</div>
  <h1 class="abs red-display call-in">Call Your Order In!</h1>

  <div class="abs cut-h" style="top:596px"></div>
  <div class="abs cut-h" style="top:902px"></div>
  <div class="abs cut-v"></div>
  <svg class="abs scissors" width="32" height="26" viewBox="0 0 32 26" aria-hidden="true">
    <g fill="none" stroke="#fff" stroke-width="2.5">
      <circle cx="6" cy="6" r="4"/><circle cx="6" cy="20" r="4"/>
      <path d="M9 8 L30 20 M9 18 L30 6"/>
    </g>
  </svg>

  <section class="coupon-extra-large">
    <div class="abs food breadsticks" role="img" aria-label="Cheesy breadsticks" style="left:30px;top:705px;width:240px;height:120px"></div>
    <div class="abs food pizza" role="img" aria-label="Extra large three topping pizza" style="left:190px;top:665px;width:265px;height:150px"></div>
    <div class="abs price-tag" style="left:28px;top:632px;width:165px;height:78px"><span class="dollars">$12</span><span class="cents">95</span></div>
    <div class="abs deal-line" style="left:34px;top:803px">1 - 16" Extra Large 3 Topping Pizza</div>
    <div class="abs deal-line" style="left:34px;top:827px">1 - 12” Medium Breadsticks with Cheese</div>
    <div class="abs expires" style="left:110px;top:856px">offer expires on 5/31/2015</div>
  </section>

  <section class="coupon-pepperoni">
    <div class="abs food pizza" role="img" aria-label="Large pepperoni pizza" style="left:612px;top:688px;width:280px;height:128px"></div>
    <div class="abs price-tag" style="left:498px;top:622px;width:130px;height:76px"><span class="dollars">$5</span><span class="cents">95</span></div>
    <div class="abs deal-line" style="left:570px;top:820px">14" Large Pepperoni Pizza</div>
    <div class="abs expires" style="left:568px;top:855px">offer expires on 5/31/2015</div>
  </section>

  <section class="coupon-family-night">
    <div class="abs food pizza" role="img" aria-label="Large two topping pizza" style="left:160px;top:915px;width:220px;height:120px"></div>
    <div class="abs food pizza" role="img" aria-label="Second large two topping pizza" style="left:220px;top:975px;width:230px;height:125px"></div>
    <div class="abs food breadsticks" role="img" aria-label="Cheesy breadsticks" style="left:30px;top:1010px;width:200px;height:90px"></div>
    <div class="abs bottle" role="img" aria-label="Two liter bottle of Zesta" style="left:392px;top:935px;width:52px;height:195px"></div>
    <div class="abs price-tag" style="left:28px;top:930px;width:165px;height:80px"><span class="dollars">$15</span><span class="cents">95</span></div>
    <div class="abs deal-title" style="left:28px;top:1044px">Family Pizza Night</div>
    <div class="abs deal-line" style="left:28px;top:1079px">2 - 14" Large 2 topping Pizzas</div>
    <div class="abs deal-line" style="left:28px;top:1103px">1 - 12” Medium Breadsticks with Cheese</div>
    <div class="abs deal-line" style="left:28px;top:1127px">1 - 2 liter of Zesta</div>
    <div class="abs expires" style="left:105px;top:1160px">offer expires on 5/31/2015</div>
  </section>

  <section class="coupon-pizza-lover">
    <div class="abs food pizza" role="img" aria-label="Medium cheese pizza" style="left:640px;top:940px;width:250px;height:105px"></div>
    <div class="abs food pizza" role="img" aria-label="Medium one topping pizza" style="left:505px;top:1015px;width:245px;height:110px"></div>
    <div class="abs food pizza" role="img" aria-label="Medium pepperoni pizza" style="left:700px;top:1020px;width:205px;height:105px"></div>
    <div class="abs price-tag" style="left:495px;top:945px;width:150px;height:80px"><span class="dollars">$11</span><span class="cents">99</span></div>
    <div class="abs deal-title" style="left:525px;top:1088px">Pizza Lover’s Deal</div>
    <div class="abs deal-line" style="left:553px;top:1129px">3 - 12” Medium 1 Topping Pizza’s</div>
    <div class="abs expires" style="left:568px;top:1160px">offer expires on 5/31/2015</div>
  </section>

</main>
</body>
</html>
```